Enter the secret world of social tradecraft

Design a stunning work of art that markets our product "Quillmark: A Hidden Ledger of Social Outreach Methods"

We need a set of assets for using in building our wordpress site and marketing materials. We'd like to have those assets delivered as a ONE PAGE HTML5 LANDING PAGE example.

We have a video that gives the look and feel of that we are going for and would like to extend it into a landing page for now with a customized logo to be included.

Watch the video here: https://www.vidloom-example.net/watch?v=QpRtLmN_7W2

The product is an informational product containing information on ZV marketing.

The final design should be intriguing and draw in the user with hints of intrigue.

Target Market(s)

Online Marketers

Industry/Entity Type

Marketing

Requirements
Must have
• Must match video in look and feel; must be html5 and responsive
Nice to have
• inventive html animations or css transitions

```html
<!DOCTYPE html>
<html lang="en">
<head>
<meta charset="utf-8">
<title>Quillmark</title>
<link href="https://fonts.googleapis.com/css2?family=Cinzel:wght@400;500;600&display=swap" rel="stylesheet">
<style>
  :root {
    --page-bg: #050505;
    --header-top: #2c2c2c;
    --header-bottom: #161616;
    --header-line: #3a3a3a;
    --menu-bg: #0c0c0c;
    --menu-bar: #9a9a9a;
    --title-ink: #f2f2f2;
    --tagline-ink: #3a3a3a;
    --frame: #454545;
    --screen: #141414;
    --control-bar: #1b1b1b;
    --control-icon: #8a8a8a;
    --progress: #c4302b;
    --play-disc: rgba(210,210,210,0.78);
    --button-bg: #f4f5f5;
    --button-ink: #111111;
    --footnote-ink: #555555;
    --hero-glow: rgba(105,105,105,0.55);
    --hero-mid: rgba(60,60,60,0.32);
  }
  * { box-sizing: border-box; margin: 0; padding: 0; }
  html, body {
    width: 1200px; height: 875px; overflow: hidden;
    background: var(--page-bg);
  }
  .landing {
    position: relative; width: 1200px; height: 875px;
    background: radial-gradient(ellipse at 50% 30%, #101010 0%, var(--page-bg) 70%);
    font-family: "Cinzel", serif;
  }
  .site-header {
    position: absolute; left: 0; top: 0; width: 1200px; height: 55px;
    background: linear-gradient(var(--header-top), var(--header-bottom));
    border-bottom: 1px solid var(--header-line);
    z-index: 2;
  }
  .menu-toggle {
    position: absolute; left: 0; top: 0; width: 59px; height: 55px;
    background: var(--menu-bg);
    border-right: 1px solid var(--header-line);
    display: flex; flex-direction: column; justify-content: center; align-items: center; gap: 5px;
  }
  .menu-toggle span { display: block; width: 34px; height: 5px; background: var(--menu-bar); }
  .site-title {
    position: absolute; left: 0; right: 0; top: 0; line-height: 55px;
    text-align: center; color: var(--title-ink);
    font-size: 30px; font-weight: 400; letter-spacing: 1px;
  }
  .hero-mark {
    position: absolute; left: 110px; top: 60px; width: 980px; height: 370px;
    background:
      radial-gradient(ellipse 300px 150px at 50% 52%, var(--hero-glow) 0%, var(--hero-mid) 55%, rgba(0,0,0,0) 100%),
      radial-gradient(ellipse 470px 190px at 50% 50%, rgba(45,45,45,0.45) 0%, rgba(25,25,25,0.25) 60%, rgba(0,0,0,0) 100%);
  }
  .video-frame {
    position: absolute; left: 384px; top: 425px; width: 440px; height: 266px;
    background: var(--frame); padding: 8px;
  }
  .video-screen {
    position: relative; width: 100%; height: 100%;
    background: radial-gradient(ellipse at 40% 45%, #262626 0%, var(--screen) 70%);
  }
  .play-button { position: absolute; left: 175px; top: 75px; }
  .video-controls {
    position: absolute; left: 0; right: 0; bottom: 0; height: 20px;
    background: var(--control-bar);
  }
  .video-progress {
    position: absolute; left: 0; right: 0; top: 0; height: 3px; background: #3a3a3a;
  }
  .video-progress::before {
    content: ""; position: absolute; left: 0; top: 0; width: 95px; height: 3px; background: var(--progress);
  }
  .tagline {
    position: absolute; left: 0; right: 0; top: 714px;
    text-align: center; color: var(--tagline-ink);
    font-size: 37px; font-weight: 600; letter-spacing: 1px; white-space: nowrap;
  }
  .enter-button {
    position: absolute; left: 479px; top: 776px; width: 250px; height: 45px;
    background: var(--button-bg); border-radius: 9px;
    color: var(--button-ink); text-decoration: none;
    font-size: 22px; line-height: 45px; text-align: center;
  }
  .footnote {
    position: absolute; left: 0; right: 0; top: 843px;
    text-align: center; color: var(--footnote-ink);
    font-family: Arial, Helvetica, sans-serif; font-size: 11px;
  }
</style>
</head>
<body>
<main class="landing">
  <header class="site-header">
    <div class="menu-toggle"><span></span><span></span><span></span></div>
    <h1 class="site-title">QUILLMARK</h1>
  </header>

  <div class="hero-mark" role="img" aria-label="Large faint sketched title lettering for Quillmark with drafting construction lines"></div>

  <div class="video-frame">
    <div class="video-screen" role="img" aria-label="Dark video still with smoky bokeh and a title card">
      <svg class="play-button" width="74" height="74" viewBox="0 0 74 74" aria-hidden="true">
        <circle cx="37" cy="37" r="37" fill="var(--play-disc)"/>
        <path d="M29 22 L53 37 L29 52 Z" fill="#222"/>
      </svg>
      <div class="video-controls">
        <div class="video-progress"></div>
        <svg width="424" height="20" viewBox="0 0 424 20" aria-hidden="true">
          <rect x="10" y="8" width="2" height="7" fill="var(--control-icon)"/>
          <rect x="14" y="8" width="2" height="7" fill="var(--control-icon)"/>
          <path d="M30 10 H33 L37 7 V16 L33 13 H30 Z" fill="var(--control-icon)"/>
          <circle cx="373" cy="11.5" r="2.5" fill="var(--control-icon)"/>
          <circle cx="387" cy="11.5" r="3" fill="none" stroke="var(--control-icon)" stroke-width="1.5"/>
          <rect x="397" y="8" width="8" height="7" fill="none" stroke="var(--control-icon)" stroke-width="1.2"/>
          <path d="M410 8 h3 M410 8 v3 M418 8 h-3 M418 8 v3 M410 15 h3 M410 15 v-3 M418 15 h-3 M418 15 v-3" stroke="var(--control-icon)" stroke-width="1.2"/>
        </svg>
      </div>
    </div>
  </div>

  <h2 class="tagline">A HIDDEN LEDGER OF SOCIAL OUTREACH METHODS</h2>
  <a class="enter-button" href="#">ENTER NOW</a>
  <p class="footnote">Copyright © 2014 Quillmark</p>
</main>
</body>
</html>
```